Dental Office Needs an Innovative Postcard Redesign

We need an updated and innovative look to our existing postcard. We would like to see creative new elements and new ways of laying out the existing offers. Please use the same colors to maintain brand consistency. Postcard size is 6 inches in height and 11 inches in width.

Industry/Entity Type

Dental

Requirements
Must have
• Stay with the brand colors and font. visit website if needed

```html
<!DOCTYPE html>
<html lang="en">
<head>
<meta charset="utf-8">
<title>Bright Arc Dental Postcard</title>
<link href="https://fonts.googleapis.com/css2?family=Mulish:wght@400;600;800&display=swap" rel="stylesheet">
<style>
:root{
  --black:#0d0d0d;
  --blue:#1f6fc4;
  --blue-edge:#0f3f78;
  --sky:#2fb2e6;
  --orange:#ee5a24;
  --white:#ffffff;
  --page:#ececec;
  --ink:#1a1a1a;
}
*{box-sizing:border-box;margin:0;padding:0}
html,body{width:1091px;height:1200px;overflow:hidden}
body{background:var(--page);font-family:"Mulish",sans-serif;color:var(--ink);position:relative}
.card{position:absolute;left:45px;width:1000px;height:545px;background:var(--white);overflow:hidden;box-shadow:0 6px 18px rgba(0,0,0,.18)}
.card--front{top:35px}
.card--back{top:620px}
.photo{position:absolute}
.photo--family{left:0;top:0;width:485px;height:460px;background:linear-gradient(160deg,#d9d4cf,#b9a79a 55%,#6b5a52)}
.photo--doctor{left:485px;top:0;width:515px;height:460px;background:linear-gradient(120deg,#f3f5f7,#dde3e8 60%,#c7d0d8)}
.photo--group{left:578px;top:55px;width:375px;height:235px;background:linear-gradient(110deg,#efe9e4,#d8cabd 55%,#e9e5e1)}
.chevron{position:absolute;left:0;top:0;width:1000px;height:180px}
.brand{position:absolute;text-align:center;color:var(--white)}
.brand__name{font-weight:600;letter-spacing:1px;line-height:1}
.brand__tag{font-weight:600;letter-spacing:3px;font-size:13px;margin-top:6px}
.card--front .brand{left:300px;width:400px;top:42px}
.card--front .brand__name{font-size:44px}

.offer{position:absolute;background:var(--blue);border:2px solid var(--white);outline:2px solid var(--blue-edge);color:var(--white);text-align:center;padding:4px 5px;display:flex;flex-direction:column;justify-content:center;align-items:center;line-height:1.05;overflow:hidden}
.offer--orange{background:var(--orange)}
.offer__big{font-weight:800;font-size:24px}
.offer__mid{font-weight:800;font-size:15px}
.offer__line{font-size:11px;font-weight:400}
.offer__fine{font-size:6px;margin-top:3px;line-height:1.2;opacity:.95}
.offer__price{font-weight:800;font-size:22px}
.offer__price small{font-size:10px;font-weight:600}

.offer--small{top:392px;height:66px;padding:3px 4px}
.offer--small .offer__big{font-size:22px}
.offer--small .offer__mid{font-size:13px}
.offer--small .offer__line{font-size:10px}
.offer--small .offer__price{font-size:18px;line-height:1.05;white-space:nowrap}
.offer--small .offer__price small{font-size:8px}
.offer--small .offer__fine{font-size:6px;margin-top:2px;white-space:nowrap}
.offer__line--tight{font-size:9.5px !important;line-height:1.1}
.nowrap{white-space:nowrap}

.strip{position:absolute;left:0;top:460px;width:1000px;height:85px;display:flex}
.strip__cta{background:var(--black);color:var(--white);width:295px;display:flex;flex-direction:column;align-items:center;justify-content:center;font-size:17px;line-height:1.15;text-align:center}
.strip__cta b{font-weight:800}
.strip__address{background:var(--orange);color:var(--white);width:395px;display:flex;flex-direction:column;align-items:center;justify-content:center;font-size:16px;font-weight:600;line-height:1.2;text-align:center}
.strip__address b{font-weight:800}
.strip__phone{background:var(--black);color:var(--white);flex:1;display:flex;align-items:center;justify-content:center;font-weight:800;font-size:40px;letter-spacing:1px}
.topline{position:absolute;left:0;top:0;width:570px;height:9px;background:var(--black);border-bottom:3px solid var(--sky)}
.map{position:absolute;left:40px;top:310px;width:232px;height:150px;background:linear-gradient(180deg,#f4f4f4,#e2e2e2);border:2px solid #9a9a9a}
.brand--back{left:287px;top:305px;width:290px;height:70px;background:var(--black);padding-top:10px}
.brand--back .brand__name{font-size:34px}
.brand--back .brand__tag{font-size:12px;margin-top:4px;letter-spacing:2px}
.address{position:absolute;right:430px;top:385px;text-align:right;font-size:16px;line-height:1.3;font-weight:600;color:var(--ink)}
.address b{font-weight:800}
.bottom{position:absolute;left:0;top:470px;height:75px;display:flex;width:597px}
.bottom .strip__cta{width:297px}
.bottom__phone{background:var(--orange);color:var(--white);flex:1;display:flex;align-items:center;justify-content:center;font-weight:800;font-size:36px;letter-spacing:1px}
</style>
</head>
<body>

<section class="card card--front">
  <div class="photo photo--family" role="img" aria-label="Photo of a smiling family lying head to head"></div>
  <div class="photo photo--doctor" role="img" aria-label="Photo of a dentist in a white coat gesturing welcome"></div>
  <svg class="chevron" viewBox="0 0 1000 180" aria-hidden="true">
    <polygon points="0,0 1000,0 1000,34 490,158 0,34" fill="#0d0d0d"/>
    <polygon points="0,34 490,158 1000,34 1000,44 490,170 0,44" fill="#2fb2e6"/>
  </svg>
  <div class="brand">
    <div class="brand__name">BRIGHT ARC</div>
    <div class="brand__tag">FAMILY | COSMETIC | IMPLANTS</div>
  </div>

  <div class="offer offer--small" style="left:12px;width:116px">
    <div class="offer__big">FREE</div>
    <div class="offer__line">Denture Consultation</div>
    <div class="offer__fine">With or without implants.</div>
  </div>
  <div class="offer offer--small offer--orange" style="left:138px;width:116px">
    <div class="offer__mid">ALWAYS FREE</div>
    <div class="offer__line">Second Opinion</div>
    <div class="offer__fine">X-rays taken if needed.</div>
  </div>
  <div class="offer offer--small" style="left:264px;width:114px">
    <div class="offer__big">FREE</div>
    <div class="offer__line">Emergency Exam<br>AND X-rays</div>
    <div class="offer__fine">New patients only.</div>
  </div>
  <div class="offer" style="left:388px;top:348px;width:198px;height:110px">
    <div class="offer__mid" style="font-size:17px">NEW PATIENT OFFER</div>
    <div style="display:flex;align-items:center;justify-content:center;gap:8px;margin-top:4px">
      <span style="font-weight:800;font-size:44px;line-height:1"><small style="font-size:20px">$</small>25</span>
      <span class="offer__line" style="text-align:left">Includes Cleaning,<br>X-rays &amp; Exam</span>
    </div>
    <div class="offer__fine">Value of $285. Not valid with other offers. Limited time. Call for details.</div>
  </div>
  <div class="offer offer--small" style="left:598px;width:118px">
    <div class="offer__line offer__line--tight">NO INSURANCE?</div>
    <div class="offer__line offer__line--tight" style="font-weight:800">NO PROBLEM!</div>
    <div class="offer__line offer__line--tight">ASK ABOUT OUR<br>IN-HOUSE<br>DISCOUNT PLAN</div>
  </div>
  <div class="offer offer--small offer--orange" style="left:726px;width:118px">
    <div class="offer__line nowrap" style="font-weight:800">ALL PORCELAIN</div>
    <div class="offer__line offer__line--tight nowrap">Caps/Crowns &amp; Veneers</div>
    <div class="offer__price"><small>Starting at </small>$597</div>
    <div class="offer__fine">Build up not included.</div>
  </div>
  <div class="offer offer--small" style="left:854px;width:134px">
    <div class="offer__line offer__line--tight nowrap">Dental Implant &amp; Crown</div>
    <div class="offer__price"><small>Starting at </small>$1997</div>
    <div class="offer__fine">Implant and crown. Call for details.</div>
  </div>

  <div class="strip">
    <div class="strip__cta"><span>SCHEDULE YOUR</span><b>APPOINTMENT TODAY!</b></div>
    <div class="strip__address"><span>1520 S. MAPLE AVE, SUITE 210</span><span>MESA VERDE, AZ 85000</span><b>WWW.BRIGHTARCDENTAL.COM</b></div>
    <div class="strip__phone">480.555.0193</div>
  </div>
</section>

<section class="card card--back">
  <div class="topline"></div>
  <div class="photo photo--group" role="img" aria-label="Photo of a multi-generation family giving thumbs up"></div>

  <div class="offer" style="left:55px;top:44px;width:235px;height:136px">
    <div class="offer__mid" style="font-size:22px">ALL PORCELAIN</div>
    <div class="offer__line" style="font-size:15px;margin-top:4px">Caps/Crowns &amp; Veneers</div>
    <div class="offer__price" style="font-size:32px;margin-top:4px"><small style="font-size:12px">Starting at </small>$597</div>
    <div class="offer__fine" style="font-size:7px">Build up not included. Insurance fees may apply. Call for details.</div>
  </div>
  <div class="offer" style="left:305px;top:38px;width:235px;height:135px">
    <div class="offer__line" style="font-size:14px">Dental Implant &amp; Crown</div>
    <div class="offer__price" style="font-size:36px;margin-top:6px"><small style="font-size:12px">Starting at </small>$1997</div>
    <div class="offer__fine" style="font-size:7px">Implant, crown and abutment included. Call for details.</div>
  </div>
  <div class="offer" style="left:45px;top:190px;width:158px;height:105px">
    <div class="offer__big" style="font-size:34px">FREE</div>
    <div class="offer__line" style="font-size:13px">Emergency Exam<br>AND X-rays</div>
    <div class="offer__fine" style="font-size:7px">New patients only. Call for details.</div>
  </div>
  <div class="offer offer--orange" style="left:215px;top:190px;width:158px;height:105px">
    <div class="offer__mid" style="font-size:22px">ALWAYS FREE</div>
    <div class="offer__line" style="font-size:13px">Second Opinion</div>
    <div class="offer__fine" style="font-size:7px">X-rays may be taken if you would like a second look.</div>
  </div>
  <div class="offer" style="left:387px;top:190px;width:158px;height:105px">
    <div class="offer__big" style="font-size:34px">FREE</div>
    <div class="offer__line" style="font-size:13px">Denture Consultation</div>
    <div class="offer__fine" style="font-size:7px">With or without implants. Call for details.</div>
  </div>

  <div class="map" role="img" aria-label="Street map showing the office location"></div>

  <div class="brand brand--back">
    <div class="brand__name">BRIGHT ARC</div>
    <div class="brand__tag">FAMILY | COSMETIC | IMPLANTS</div>
  </div>
  <div class="address">1520 S. MAPLE AVE, SUITE 210<br>MESA VERDE, AZ 85000<br><b>WWW.BRIGHTARCDENTAL.COM</b></div>

  <div class="bottom">
    <div class="strip__cta"><span>SCHEDULE YOUR</span><b>APPOINTMENT TODAY!</b></div>
    <div class="bottom__phone">480.555.0193</div>
  </div>
</section>

</body>
</html>
```